International research group on Amber Lantern; needs a bold, futuristic website*

We need a website and logo design for our research programme. Our research programme is about how we can build an inclusive future for our societies, at a time when there are pressures for digital technologies to be used to take away jobs and/or create precarious work. Our website is meant to provide actors in society with the latest evidence so that they can act on them to introduce new policies, programmes and activities that support human augmentation. We push our research findings through the website, as they emerge. We want the website to be futuristic and bold, but with a sense of inclusion, compassion and the preservation of human civilization in an age of machines. Pls see the uploaded file for the project brief.
Updates

Target Market(s)

• Primary: Researchers & Policy-makers
• Secondary:
a) Industry – C-suite including Chief Technology Officers, Chief Human Resource Officers
b) Practitioners – Digital consultants, jobs & skills analysts, educators, technologists, journalists

Logo Text

Amber Lantern Collective

Coding

Coded - Design and coding required

Number of Pages Required

5+ page

Font styles to use
Sans Serif

Requirements
Must have
• 1) Feature of the month
2) Repository of documents that is attractive, with highlights and easy markers for different types of stakeholders
3) Blog postings
Nice to have
• Pls see two websites we kind of like:
https://brindlequay.example/
https://www.wegstein-lorv.example/en/

```html
<!DOCTYPE html>
<html lang="en">
<head>
<meta charset="utf-8">
<title>Amber Lantern Collective</title>
<link href="https://fonts.googleapis.com/css2?family=IBM+Plex+Sans:wght@400;500;600;700&display=swap" rel="stylesheet">
<style>
:root{
  --brand:#1d4e8f;
  --brand-dark:#163c70;
  --ink:#1b1b1b;
  --text:#3d3d3d;
  --paper:#ffffff;
  --mist:#f3f1f2;
  --hero-a:#6a1fb0;
  --hero-b:#2b1a8e;
  --hero-line:#5ee0ff;
  --night:#1f1f21;
  --night-line:#3a3a3d;
  --accent-green:#19c39a;
}
*{box-sizing:border-box;margin:0;padding:0}
html,body{width:1200px;height:3967px;overflow:hidden}
body{font-family:"IBM Plex Sans",Arial,sans-serif;color:var(--text);background:var(--paper);position:relative}
.abs{position:absolute}
.btn{position:absolute;display:flex;align-items:center;justify-content:center;background:var(--brand);color:#fff;font-weight:600;letter-spacing:.5px;text-transform:uppercase}
.rule{position:absolute;height:2px;background:var(--brand);width:52px}
h2.section-title{position:absolute;font-size:24px;font-weight:700;color:var(--ink);letter-spacing:.3px;text-transform:uppercase}
.copy{position:absolute;font-size:14.5px;line-height:20.8px;color:var(--text)}

/* hero */
.hero{position:absolute;left:0;top:0;width:1200px;height:632px;background:linear-gradient(120deg,var(--hero-a) 0%,#4a1aa6 45%,var(--hero-b) 100%);overflow:hidden}
.hero-art{position:absolute;left:585px;top:60px;width:430px;height:572px;background:radial-gradient(ellipse at 55% 45%,rgba(94,224,255,.35),rgba(94,224,255,.08) 60%,transparent 75%)}
.brand{position:absolute;display:flex;align-items:center;gap:12px;color:#fff;font-weight:700;text-transform:uppercase;white-space:nowrap}
.brand .dot{width:30px;height:30px;border-radius:50%;background:#fff}
.nav{position:absolute;left:595px;top:32px;display:flex;gap:34px;color:#fff;font-weight:600;font-size:16px;letter-spacing:.3px}
.hero h1{position:absolute;left:132px;top:244px;color:#fff;font-size:42px;line-height:50px;font-weight:700;letter-spacing:1px}
.hero .ghost{position:absolute;left:134px;top:367px;width:139px;height:43px;border:2px solid #fff;color:#fff;font-weight:600;font-size:17px;display:flex;align-items:center;justify-content:center;letter-spacing:.5px}

/* documents */
.docs{position:absolute;left:0;top:632px;width:1200px;height:531px;background:var(--mist)}
.doc-card{position:absolute;top:58px;width:299px;height:411px;background:#fff;box-shadow:0 2px 10px rgba(0,0,0,.06);text-align:center}
.doc-card svg{position:absolute;left:112px;top:38px}
.doc-card h3{position:absolute;top:141px;left:0;width:100%;font-size:16.5px;font-weight:500;color:var(--ink);letter-spacing:.3px}
.doc-card p{position:absolute;left:30px;top:198px;width:239px;font-size:12.3px;line-height:17.6px;color:var(--text)}
.doc-card .btn{left:104px;top:345px;width:91px;height:26px;font-size:10.5px}

.photo{position:absolute}
.commentaries{position:absolute;left:0;top:1642px;width:1200px;height:471px;background:var(--mist)}

/* blog */
.blog-card{position:absolute;top:2247px;width:301px;height:385px;background:#fff;border:1px solid #d6d6d6}
.blog-card .thumb{position:absolute;left:0;top:0;width:100%;height:208px}
.blog-card h4{position:absolute;left:24px;top:229px;width:260px;font-size:13px;line-height:20px;font-weight:500;color:var(--ink);text-transform:uppercase}
.blog-card p{position:absolute;left:24px;top:274px;width:255px;font-size:11.5px;line-height:16px;color:#555}
.blog-card .btn{left:26px;top:337px;width:80px;height:22px;font-size:9.5px}

.video{position:absolute;left:0;top:2680px;width:1200px;height:431px;background:linear-gradient(180deg,#2f6db5 0%,#1f4f93 60%,#1a437f 100%)}
.play{position:absolute;left:568px;top:163px;width:64px;height:64px;border-radius:50%;border:3px solid #fff;display:flex;align-items:center;justify-content:center}
.arrow{position:absolute;top:2878px;width:34px;height:34px;background:#fff;display:flex;align-items:center;justify-content:center}

.feature{position:absolute;left:0;top:3111px;width:1200px;height:496px;background:var(--mist)}

/* footer */
.footer{position:absolute;left:0;top:3607px;width:1200px;height:360px;background:var(--night);color:#fff}
.footer h5{position:absolute;font-size:13px;font-weight:700;letter-spacing:.5px}
.menu-list{position:absolute;left:651px;top:94px;list-style:none;font-size:12px;line-height:20px;color:#ddd}
.contact-row{position:absolute;left:853px;display:flex;gap:10px;font-size:12px;line-height:16px;color:#ddd}
.contact-row .ico{width:22px;height:22px;border-radius:50%;background:#fff;display:flex;align-items:center;justify-content:center;flex:none}
.social{position:absolute;top:311px;display:flex;align-items:center;font-size:12px;font-weight:600}
</style>
</head>
<body>

<header class="hero">
  <div class="hero-art" role="img" aria-label="Illustration of a glowing circuit-line human head in profile over a grid of digital code"></div>
  <div class="brand" style="left:134px;top:38px;font-size:26px"><span class="dot"></span>Amber Lantern Collective</div>
  <nav class="nav"><span>HOME</span><span>ABOUT US</span><span>SERVICES</span><span>BLOG</span><span>CONTACT US</span></nav>
  <h1>HUMAN-MACHINE<br>AUGMENTATION</h1>
  <div class="ghost">READ MORE</div>
</header>

<section class="docs">
  <article class="doc-card" style="left:123px">
    <svg width="75" height="75" viewBox="0 0 75 75"><rect x="22" y="2" width="36" height="48" fill="none" stroke="var(--brand)" stroke-width="3"/><rect x="16" y="8" width="36" height="48" fill="none" stroke="var(--brand)" stroke-width="3"/><rect x="8" y="14" width="38" height="52" fill="var(--brand)"/><circle cx="24" cy="36" r="8" fill="none" stroke="#fff" stroke-width="3"/><line x1="30" y1="42" x2="37" y2="50" stroke="#fff" stroke-width="3"/></svg>
    <h3>RESEARCH REPORTS</h3>
    <p>Lorem ipsum dolor sit amet consec tetur adipiscing elit, sed do eiusmod tempor incididunt ut labore et dolore magna aliq ua. Ut enim ad minim veniam quis x ea commodo consequat. Duis aute irure dolor in reprehenderit in voluptate velit esse cillum dolore</p>
    <div class="btn">Read More</div>
  </article>
  <article class="doc-card" style="left:450px">
    <svg width="75" height="75" viewBox="0 0 75 75"><path d="M14 6h34l14 14v50H14z" fill="var(--brand)"/><path d="M48 6v14h14" fill="#fff" opacity=".5"/><g stroke="#fff" stroke-width="3"><line x1="22" y1="30" x2="54" y2="30"/><line x1="22" y1="38" x2="54" y2="38"/><line x1="22" y1="46" x2="54" y2="46"/><line x1="22" y1="54" x2="54" y2="54"/><line x1="22" y1="62" x2="44" y2="62"/></g></svg>
    <h3>WORKING PAPERS</h3>
    <p>Lorem ipsum dolor sit amet consec tetur adipiscing elit, sed do eiusmod tempor incididunt ut labore et dolore magna aliq ua. Ut enim ad minim veniam quis x ea commodo consequat. Duis aute irure dolor in reprehenderit in voluptate velit esse cillum dolore</p>
    <div class="btn">Read More</div>
  </article>
  <article class="doc-card" style="left:778px">
    <svg width="75" height="75" viewBox="0 0 75 75" fill="none" stroke="var(--brand)" stroke-width="4"><path d="M20 8h38v52a8 8 0 0 1-8 8H14a8 8 0 0 1-8-8v-6h36v6a8 8 0 0 0 8 8"/><path d="M20 8a6 6 0 0 0-6 6v6h6"/><line x1="28" y1="22" x2="50" y2="22"/><line x1="28" y1="32" x2="50" y2="32"/><line x1="28" y1="42" x2="50" y2="42"/></svg>
    <h3>BRIEFING PAPERS</h3>
    <p>Lorem ipsum dolor sit amet consec tetur adipiscing elit, sed do eiusmod tempor incididunt ut labore et dolore magna aliq ua. Ut enim ad minim veniam quis x ea commodo consequat. Duis aute irure dolor in reprehenderit in voluptate velit esse cillum dolore</p>
    <div class="btn">Read More</div>
  </article>
</section>

<section class="practitioners">
  <div class="photo" style="left:132px;top:1209px;width:453px;height:384px;background:linear-gradient(135deg,#c9ccd1,#5d6570 55%,#2e3440)" role="img" aria-label="Photo of colleagues talking around a meeting table in an office"></div>
  <h2 class="section-title" style="left:628px;top:1238px">NOTES FOR PRACTITIONERS</h2>
  <div class="rule" style="left:628px;top:1279px"></div>
  <p class="copy" style="left:629px;top:1311px;width:445px">At vero eos et accusamus et iusto odio dignissimos ducimus qui blanditiis praesentium voluptatum deleniti atque corrupti quos dolores et quas molestias excepturi sint occaecati cupiditate non provident, similique sunt in culpa qui officia deserunt mollitia animi, id est laborum et dolorum fuga. Et harum quidem rerum facilis est et expedita distinctio. Nam libero tempore, cum soluta nobis est eligendi optio cumque nihil impedit quo minus id quod maxime placeat facere possimus, omnis voluptas assumenda est, omnis dolor repellendus. Temporibus autem quibusdam et aut officiis</p>
  <div class="btn" style="left:631px;top:1531px;width:103px;height:30px;font-size:12.5px">Read More</div>
</section>

<section class="commentaries">
  <h2 class="section-title" style="left:131px;top:67px">COMMENTARIES</h2>
  <div class="rule" style="left:131px;top:108px"></div>
  <p class="copy" style="left:132px;top:141px;width:445px">At vero eos et accusamus et iusto odio dignissimos ducimus qui blanditiis praesentium voluptatum deleniti atque corrupti quos dolores et quas molestias excepturi sint occaecati cupiditate non provident, similique sunt in culpa qui officia deserunt mollitia animi, id est laborum et dolorum fuga. Et harum quidem rerum facilis est et expedita distinctio. Nam libero tempore, cum soluta nobis est eligendi optio cumque nihil impedit quo minus id quod maxime placeat facere possimus, omnis voluptas assumenda est, omnis dolor repellendus. Temporibus autem quibusdam et aut officiis</p>
  <div class="btn" style="left:135px;top:360px;width:103px;height:31px;font-size:12.5px">Read More</div>
  <div class="photo" style="left:613px;top:38px;width:453px;height:385px;background:linear-gradient(160deg,#dfe4e8,#8e99a3 50%,#3c4650)" role="img" aria-label="Photo of a presenter standing at the head of a glass-walled boardroom table"></div>
</section>

<section class="blog">
  <h2 class="section-title" style="left:0;width:1200px;text-align:center;top:2161px">LATEST BLOG</h2>
  <div class="rule" style="left:565px;top:2209px;width:70px"></div>
  <article class="blog-card" style="left:134px">
    <div class="thumb" style="background:linear-gradient(135deg,#e3e0da,#8a8f96 60%,#4a4f57)" role="img" aria-label="Photo of three colleagues gathered around a laptop"></div>
    <h4>On the other hand we denounce with righteous indignation</h4>
    <p>At vero eos et accusamus et iusto odio digni ssimos ducimus qui blanditiis praesentium and dislike men who are so beguiled</p>
    <div class="btn">Read More</div>
  </article>
  <article class="blog-card" style="left:450px">
    <div class="thumb" style="background:linear-gradient(100deg,#0e1620,#1c3a55 50%,#3f7ba3)" role="img" aria-label="Photo of a person in glasses beside a circuit-pattern head illustration"></div>
    <h4>At vero eos et accusamus et iusto odio dignissimos ducimus</h4>
    <p>At vero eos et accusamus et iusto odio digni ssimos ducimus qui blanditiis praesentium and dislike men who are so beguiled</p>
    <div class="btn">Read More</div>
  </article>
  <article class="blog-card" style="left:765px">
    <div class="thumb" style="background:radial-gradient(ellipse at 65% 40%,#2d7fd0,#0b2a66 55%,#06133a)" role="img" aria-label="Illustration of a glowing blue wireframe head on a dark background"></div>
    <h4>Sed ut perspiciatis unde omnis iste natus error sit voluptatem</h4>
    <p>At vero eos et accusamus et iusto odio digni ssimos ducimus qui blanditiis praesentium and dislike men who are so beguiled</p>
    <div class="btn">Read More</div>
  </article>
</section>

<section class="video" role="img" aria-label="Blue-tinted photo of a team working together around a table, with a video play control">
  <div class="play"><svg width="22" height="26" viewBox="0 0 22 26"><path d="M3 2l17 11-17 11z" fill="#fff"/></svg></div>
  <div class="abs" style="left:0;width:1200px;text-align:center;top:237px;color:#fff;font-size:16px;font-weight:500">PLAY VIDEO</div>
</section>
<div class="arrow" style="left:0"><svg width="12" height="16" viewBox="0 0 12 16"><path d="M9 2L3 8l6 6" fill="none" stroke="var(--brand)" stroke-width="2.5"/></svg></div>
<div class="arrow" style="left:1166px"><svg width="12" height="16" viewBox="0 0 12 16"><path d="M3 2l6 6-6 6" fill="none" stroke="var(--brand)" stroke-width="2.5"/></svg></div>

<section class="feature">
  <h2 class="section-title" style="left:0;width:1200px;text-align:center;top:40px">FEATURE OF THE MONTH</h2>
  <div class="rule" style="left:565px;top:88px;width:70px"></div>
  <div class="abs" style="left:134px;top:129px;width:932px;height:317px;background:#fff">
    <div class="photo" style="left:0;top:0;width:471px;height:317px;background:linear-gradient(135deg,#f2f2f2,#b9bec4 55%,#5c636b)" role="img" aria-label="Photo of hands gesturing over a laptop and printed charts"></div>
    <h4 class="abs" style="left:513px;top:42px;width:300px;font-size:13.5px;line-height:20px;font-weight:700;color:var(--ink)">SED UT PERSPICIATIS UNDE OMNIS ISTE NATUS ERROR SIT VOLUPTATEM</h4>
    <p class="abs" style="left:513px;top:91px;width:372px;font-size:12.3px;line-height:17.3px;color:var(--text)">At vero eos et accusamus et iusto odio dignissimos ducimus qui blanditiis praesentium voluptatum deleniti atque corrupti quos dolores et quas molestias excepturi sint occaecati cupiditate non provident, similique sunt in culpa qui officia deserunt mollitia animi, id est laborum et dolorum fuga. Et harum quidem rerum facilis est et expedita distinctio. Nam libero tempore, cum soluta nobis est eligendi optio cumque nihil impedit quo minus id quod maxime placeat facer.</p>
    <div class="btn" style="left:513px;top:248px;width:103px;height:31px;font-size:12.5px">Read More</div>
  </div>
</section>

<footer class="footer">
  <div class="brand" style="left:122px;top:118px;font-size:26px"><span class="dot"></span>Amber Lantern Collective</div>
  <h5 style="left:651px;top:58px">MENU</h5>
  <ul class="menu-list"><li>HOME</li><li>ABOUT US</li><li>SERVICES</li><li>BLOG</li><li>CONTACT US</li></ul>
  <h5 style="left:853px;top:58px">CONTACT US</h5>
  <div class="contact-row" style="top:94px"><span class="ico"><svg width="10" height="13" viewBox="0 0 10 13"><path d="M5 0a5 5 0 0 1 5 5c0 4-5 8-5 8S0 9 0 5a5 5 0 0 1 5-5z" fill="var(--night)"/><circle cx="5" cy="5" r="1.8" fill="#fff"/></svg></span><span>72 Harrowgate Lane<br>Fenmore, CA 90000</span></div>
  <div class="contact-row" style="top:145px"><span class="ico"><svg width="12" height="12" viewBox="0 0 12 12"><path d="M2 1l2.5 0 1 3-1.5 1a7 7 0 0 0 3 3l1-1.5 3 1V10a1 1 0 0 1-1 1A10 10 0 0 1 1 2a1 1 0 0 1 1-1z" fill="var(--night)"/></svg></span><span>Call Us<br>555.014.2290</span></div>
  <div class="contact-row" style="top:196px"><span class="ico"><svg width="12" height="9" viewBox="0 0 12 9"><rect width="12" height="9" fill="var(--night)"/><path d="M0 0l6 5 6-5" fill="none" stroke="#fff" stroke-width="1"/></svg></span><span>E mail Us<br>info@AmberLanternCollective.example</span></div>
  <div class="abs" style="left:134px;top:269px;width:935px;height:1px;background:var(--night-line)"></div>
  <div class="social" style="left:145px;gap:26px">
    <span>FOLLOW US</span>
    <span style="font-weight:500">Chirpline</span>
    <span style="background:var(--accent-green);padding:6px 12px;font-weight:500;font-size:10.5px">PaperCommons</span>
    <span style="font-weight:500">ClipStream</span>
  </div>
  <div class="abs" style="left:893px;top:316px;font-size:10px;color:#ccc">Copyright © 2020 All Rights Reserved</div>
</footer>

</body>
</html>
```